Trvmlegal.com needs a wedsite. Law Office of Darnell P. Whitby

Darnell P. Whitby is a criminal law firm that is 5 years old. We have already had all the content written and now just need the website designed. We also just finished our logo design using Pixel Harbor and would like it used in the design of the website.

Industry/Entity Type

Law Firm

Number of Pages Required

5+ page

Requirements
Must have
• I was our new logo to be on the website also. I want Dallas sites as the stock pictures for the website. For example the Grey Stone Tribunal. I also need to be able to add YouTube videos. It has to adjust to be seen on computers and also cell phones. I need to be able to have a information sheet for clients to fill out and submit back to me.

```html
<!DOCTYPE html>
<html lang="en">
<head>
<meta charset="utf-8">
<title>Law Office of Darnell P. Whitby</title>
<link rel="stylesheet" href="https://fonts.googleapis.com/css2?family=Open+Sans:wght@400;600;700&family=Arimo:wght@400&display=swap">
<style>
:root{
  --blue:#0a9bdc;
  --blue-dark:#0b7fc0;
  --navy:#173a80;
  --ink:#1e1e1e;
  --text:#3a3a3a;
  --panel:#f0f0f0;
  --footer:#2c2c2c;
  --white:#ffffff;
  --rule:#d4d4d4;
}
*{box-sizing:border-box;margin:0;padding:0}
html,body{width:915px;height:1200px;overflow:hidden;background:var(--white)}
body{font-family:"Open Sans",Arial,sans-serif;color:var(--text);position:relative}
.abs{position:absolute}

/* header */
.site-header{left:0;top:0;width:915px;height:72px;background:var(--white);z-index:2}
.brand-circle{left:122px;top:10px;width:140px;height:140px;border-radius:50%;background:#a9d6ea;z-index:3}
.brand-name{left:278px;top:18px;font-weight:700;font-size:15px;line-height:19px;color:var(--navy);z-index:3}
.main-nav{left:470px;top:29px;display:flex;gap:23px;font-size:11px;color:var(--ink);letter-spacing:.2px}
.social{top:24px;width:25px;height:25px;border-radius:50%;background:var(--blue)}

/* hero */
.hero{left:0;top:72px;width:915px;height:428px;
  background:radial-gradient(ellipse at 68% 60%,#7fd3f5 0%,#2aa9e6 30%,#0f78b8 62%,#06406e 100%)}
.hero-title{left:112px;top:178px;font-family:"Arimo",Arial,sans-serif;font-size:30px;color:var(--white);letter-spacing:.5px}
.hero-copy{left:112px;top:220px;width:335px;font-size:11.2px;line-height:21.5px;color:var(--white)}
.hero-btn{left:113px;top:325px;width:85px;height:35px;border:1px solid var(--white);border-radius:4px;color:var(--white);font-size:11.5px;display:flex;align-items:center;justify-content:center}
.hero-dots{left:112px;top:461px;display:flex;gap:4px}
.hero-dots span{width:9px;height:9px;border-radius:50%;border:1px solid var(--white)}
.hero-dots span.active{background:var(--white)}

/* intro */
.intro-kicker{left:107px;top:525px;font-size:16.5px;font-weight:700;color:var(--ink)}
.intro-title{left:107px;top:550px;font-size:16.5px;font-weight:700;color:var(--blue)}
.dotted-rule{height:4px;background:repeating-linear-gradient(90deg,var(--rule) 0 1px,transparent 1px 2px)}
.intro-rule{left:107px;top:582px;width:702px}
.intro-copy{left:107px;top:603px;width:705px;font-size:9.6px;line-height:20px;color:var(--text);text-align:justify}

/* services */
.services{left:0;top:706px;width:915px;height:341px;background:var(--panel)}
.svc-icon{width:62px;height:62px;border-radius:50%;background:var(--blue);border:3px solid var(--white);box-shadow:0 0 0 1px #dcdcdc;display:flex;align-items:center;justify-content:center}
.svc-title{font-size:12.8px;font-weight:700;color:var(--blue);letter-spacing:.1px}
.svc-rule{width:228px}
.svc-copy{width:230px;font-size:9.6px;line-height:17.6px;color:var(--text);text-align:justify}

/* footer */
.footer{left:0;top:1047px;width:915px;height:96px;background:var(--footer)}
.foot-circle{left:135px;top:1057px;width:80px;height:80px;border-radius:50%;background:#cfcfcf}
.foot-name{left:152px;top:1082px;width:50px;font-size:8px;font-weight:700;line-height:10px;color:var(--footer);text-align:center}
.foot-divider{top:1060px;width:1px;height:72px;background:#9a9a9a}
.foot-text{font-family:Arial,sans-serif;font-size:10px;color:var(--white)}
.foot-btn{left:695px;top:1081px;width:113px;height:31px;border-radius:3px;background:var(--blue);color:var(--white);font-size:10px;display:flex;align-items:center;justify-content:center;letter-spacing:.3px}
.copyright{left:0;top:1143px;width:915px;height:57px;background:var(--blue);color:var(--white);font-family:Arial,sans-serif;font-size:10px;display:flex;align-items:center;justify-content:center}
</style>
</head>
<body>

<header class="abs site-header"></header>
<div class="abs brand-circle"></div>
<div class="abs brand-name">Law Office of<br>Darnell P. Whitby</div>
<nav class="abs main-nav"><span>ABOUT</span><span>SERVICES</span><span>PEOPLE</span><span>CONTACT</span></nav>
<span class="abs social" style="left:714px" aria-label="Social link"></span>
<span class="abs social" style="left:749px" aria-label="Social link"></span>
<span class="abs social" style="left:784px" aria-label="Social link"></span>

<section class="abs hero" role="img" aria-label="Blue-toned photograph of brass scales of justice on a desk"></section>
<h1 class="abs hero-title">LAW OFFICE OF</h1>
<p class="abs hero-copy">Consectetuer adipiscing elit. Aenean commodo ligula eget dolor. Aenean massa. Cum sociis natoque penatibus et magnis dis parturient montes, nascetur ridiculus mus. Donec quam felis, ultricies nec, pellentesque eu, pretium quis, sem. Nulla consequat massa quis enim.</p>
<div class="abs hero-btn">Read More</div>
<div class="abs hero-dots"><span class="active"></span><span></span><span></span><span></span></div>

<h2 class="abs intro-kicker">IMPACTFUL. VALUABLE. TRUSTED.</h2>
<h3 class="abs intro-title">THAT’S HOW YOU SHOULD THINK OF YOUR LAWYERS, RIGHT?</h3>
<div class="abs dotted-rule intro-rule"></div>
<p class="abs intro-copy">Big Law plays an important part in the legal services industry. While you get the resources of a large organization, the services are costly and mis-incentivized so your lawyers benefit from taking longer and chasing every angle, regardless of whether it makes the most sense for your needs and budget. Been there, seen that. Harlow Legal is committed to making your life easier. To explore and listen to your true needs. To provide simple explanations that enable you to make the right business decisions. Harlow Legal is fully committed to providing high-impact work at an unquestionable value to help you achieve great success. And to earning your unwavering trust for the long haul.</p>

<section class="abs services"></section>

<div class="abs svc-icon" style="left:109px;top:736px">
  <svg width="30" height="22" viewBox="0 0 30 22"><rect x="2" y="12" width="26" height="3" fill="#fff"/><rect x="5" y="15" width="2" height="6" fill="#fff"/><rect x="23" y="15" width="2" height="6" fill="#fff"/></svg>
</div>
<h4 class="abs svc-title" style="left:186px;top:741px">OUTSIDE GENERAL COUNSEL</h4>
<div class="abs dotted-rule svc-rule" style="left:186px;top:763px"></div>
<p class="abs svc-copy" style="left:187px;top:778px">Maybe you have an in-house counsel, or maybe you don't. Harlow Legal can provide you with the in-house counsel services your company needs so your employees can focus on their primary jobs.</p>

<div class="abs svc-icon" style="left:487px;top:736px">
  <svg width="30" height="30" viewBox="0 0 30 30"><g transform="rotate(-40 15 13)" fill="#fff"><rect x="8" y="6" width="14" height="7" rx="1"/><rect x="13.5" y="13" width="3" height="12"/></g><rect x="4" y="25" width="14" height="3" fill="#fff"/></svg>
</div>
<h4 class="abs svc-title" style="left:563px;top:741px">LITIGATION AND DISPUTE RESOLUTION</h4>
<div class="abs dotted-rule svc-rule" style="left:563px;top:763px;width:245px"></div>
<p class="abs svc-copy" style="left:564px;top:778px;width:243px">Business disputes can be very expensive and disruptive. Harlow Legal can vigorously fight to resolve business disputes favorably, and more importantly help you anticipate problems at the outset to prevent them in the future.</p>

<div class="abs svc-icon" style="left:109px;top:871px">
  <svg width="30" height="22" viewBox="0 0 30 22"><rect x="4" y="9" width="22" height="3" fill="#fff"/><rect x="7" y="12" width="2" height="8" fill="#fff"/><rect x="21" y="12" width="2" height="8" fill="#fff"/></svg>
</div>
<h4 class="abs svc-title" style="left:184px;top:876px">EMPLOYMENT CONSULTING.</h4>
<div class="abs dotted-rule svc-rule" style="left:186px;top:898px"></div>
<p class="abs svc-copy" style="left:187px;top:913px">Hiring, NDAs and non-compete agreements, policies and handbooks, separations, disputes. Harlow Legal has experience counseling to avoid employment issues and in problem solving and working them out.</p>

<div class="abs svc-icon" style="left:487px;top:871px">
  <svg width="26" height="30" viewBox="0 0 26 30"><rect x="3" y="3" width="17" height="24" fill="none" stroke="#fff" stroke-width="2"/><g fill="#fff"><rect x="6" y="8" width="11" height="2"/><rect x="6" y="12" width="11" height="2"/><rect x="6" y="16" width="11" height="2"/><rect x="6" y="20" width="8" height="2"/></g><rect x="22" y="6" width="2" height="23" fill="#fff"/></svg>
</div>
<h4 class="abs svc-title" style="left:565px;top:876px">BUSINESS DOCUMENTS.</h4>
<div class="abs dotted-rule svc-rule" style="left:563px;top:898px;width:245px"></div>
<p class="abs svc-copy" style="left:564px;top:913px;width:243px">Why frown about creating a new agreement or sweat over what someone else may be slipping into their form? Harlow Legal is experienced in drafting, reviewing and negotiating many types of business agreements, including real estate agreements and leases, business organization documents, and commercial contracts of many kinds.</p>

<footer class="abs footer"></footer>
<div class="abs foot-circle"></div>
<div class="abs foot-name">Darnell P. Whitby</div>
<div class="abs foot-divider" style="left:281px"></div>
<div class="abs foot-divider" style="left:458px"></div>
<div class="abs foot-divider" style="left:655px"></div>
<svg class="abs" style="left:318px;top:1077px" width="10" height="14" viewBox="0 0 10 14"><path d="M5 0a5 5 0 0 1 5 5c0 4-5 9-5 9S0 9 0 5a5 5 0 0 1 5-5z" fill="#fff"/><circle cx="5" cy="5" r="2" fill="#2c2c2c"/></svg>
<div class="abs foot-text" style="left:337px;top:1079px">418 MARLOW ST.</div>
<div class="abs foot-text" style="left:338px;top:1100px">Your Address</div>
<svg class="abs" style="left:484px;top:1080px" width="12" height="10" viewBox="0 0 12 10"><rect x="0" y="0" width="12" height="3" rx="1" fill="#fff"/><rect x="2" y="4" width="8" height="6" rx="1" fill="#fff"/></svg>
<div class="abs foot-text" style="left:506px;top:1079px">555-014-2278</div>
<svg class="abs" style="left:485px;top:1102px" width="11" height="8" viewBox="0 0 11 8"><rect width="11" height="8" fill="#fff"/><path d="M0 0l5.5 4.5L11 0" fill="none" stroke="#2c2c2c" stroke-width="1"/></svg>
<div class="abs foot-text" style="left:501px;top:1101px">Your copmany name.</div>
<div class="abs foot-btn">GET IN TOUCH</div>
<div class="abs copyright">Copyright 2015 © Your company name. All Right reserved. Site Map I Privacy Policy</div>

</body>
</html>
```